Website design: Mobile Physiotherapy, Massage & Personal Training Business

I need a website that reflects a staff of health and fitness professionals. I would like the theme of the website to match the company logo (Summit Motion Wellness).
This is a link for a competitors website that I am fond of:
http://www.brackenrehab.com.au/
I am open to any and all creative and innovative designs.

```html
<!DOCTYPE html>
<html lang="en">
<head>
<meta charset="utf-8">
<title>Summit Motion Wellness</title>
<link href="https://fonts.googleapis.com/css2?family=Exo+2:wght@400;500;600&family=Open+Sans:ital,wght@0,400;0,600;0,700;1,400&display=swap" rel="stylesheet">
<style>
:root{
  --red:#ef4f5a;
  --red-dark:#d3232f;
  --red-text:#e0323d;
  --grey-band:#555657;
  --page:#f4f4f4;
  --white:#ffffff;
  --ink:#333333;
  --muted:#8a8a8a;
  --line:#dddddd;
  --track:#d9d9d9;
}
*{box-sizing:border-box;margin:0;padding:0}
html,body{width:1200px;height:3900px;overflow:hidden}
body{background:var(--page);font-family:"Open Sans",Arial,sans-serif;color:var(--ink);position:relative}
section,header,footer{position:absolute;left:0;width:1200px}
.abs{position:absolute}
h2.section-title{font-family:"Exo 2",Arial,sans-serif;font-weight:500;font-size:30px;letter-spacing:1px;color:#2b2b2b;text-transform:uppercase}
.centered-title{left:0;width:1200px;text-align:center}
.centered-title::after{content:"";display:block;width:60px;height:2px;background:#bbb;margin:12px auto 0}
.body-text{font-size:13px;line-height:20px;color:var(--muted)}
.btn{display:inline-block;background:var(--red-dark);color:#fff;font-size:12px;font-weight:700;padding:9px 18px;border-radius:2px}
.photo{display:block}

/* header */
.site-header{top:0;height:590px;background:linear-gradient(180deg,#e6e6e6,#cfcfcf)}
.brand{left:180px;top:38px;display:flex;align-items:center;gap:10px}
.brand-dot{width:22px;height:22px;border-radius:50%;background:var(--red-dark)}
.brand-name{font-family:"Open Sans",Arial,sans-serif;font-weight:700;font-size:22px;color:var(--red-dark)}
.main-nav{left:565px;top:38px;display:flex;background:#fff;box-shadow:0 1px 3px rgba(0,0,0,.15)}
.main-nav a{font-size:12px;color:#555;padding:9px 14px;text-transform:uppercase;text-decoration:none}
.main-nav a.active{background:var(--red-dark);color:#fff}
.hero{left:180px;top:110px;width:840px;height:410px;background:linear-gradient(160deg,#6d86b8 0%,#a07070 45%,#b77a5a 70%,#8f6b5f 100%)}

/* about */
.about{top:590px;height:360px;background:var(--page)}
.about .section-title{left:180px;top:40px}
.about .body-text{left:180px;width:400px}
.video{left:615px;top:43px;width:405px;height:232px;background:linear-gradient(135deg,#8a8d92,#4e5257)}
.video-bar{left:0;bottom:0;width:405px;height:26px;background:#1c1c1c}
.play{left:172px;top:86px;width:60px;height:42px;background:#222;border-radius:8px;opacity:.9}

/* red feature bands */
.feature-band{height:380px;background:var(--red)}
.feature-intro{left:180px;top:40px;width:198px;height:290px;background:var(--red-dark);color:#fff;padding:42px 20px 0}
.feature-intro h3{font-family:"Exo 2",Arial,sans-serif;font-weight:500;font-size:16px;text-transform:uppercase;border-bottom:1px solid rgba(255,255,255,.5);padding-bottom:10px;margin-bottom:10px}
.feature-intro p{font-size:12px;line-height:17px}
.arrows{position:absolute;left:20px;top:184px;display:flex;gap:10px}
.arrow-btn{width:36px;height:36px;border:1px solid rgba(255,255,255,.8);display:flex;align-items:center;justify-content:center}
.card{top:40px;width:195px;height:290px;background:#fff}
.card .photo{width:195px;height:198px}
.card-label{position:absolute;top:226px;left:0;width:195px;text-align:center;font-size:15px;color:#333}
.card-label::after{content:"";display:block;width:64px;height:2px;background:#444;margin:18px auto 0}

/* news */
.news{top:1330px;height:470px}
.news .section-title{top:40px}
.post-date{font-size:12px;color:#aaa}
.post-title{font-family:"Exo 2",Arial,sans-serif;font-weight:500;font-size:25px;line-height:32px;color:var(--red-text)}
.tip-title{font-family:"Exo 2",Arial,sans-serif;font-weight:500;font-size:20px;color:var(--red-text)}
.tip-title::before{content:"› ";}

/* team */
.team{top:1800px;height:290px;background:var(--grey-band)}
.team-photo{left:396px;top:45px;width:267px;height:195px;background:linear-gradient(135deg,#9aa0a4,#6d5b56 60%,#c04050)}
.team-card{left:681px;top:45px;width:339px;height:195px;background:#fff;padding:30px 22px}
.team-card h4{font-family:"Exo 2",Arial,sans-serif;font-weight:500;font-size:16px;text-transform:uppercase;color:#333;margin-bottom:14px}

/* testimonials */
.testimonials{top:2090px;height:410px;background:var(--page)}
.avatar{left:560px;top:122px;width:80px;height:80px;border-radius:50%;background:linear-gradient(135deg,#d7b9a5,#b59078);border:3px solid #fff}
.quote{left:240px;top:218px;width:720px;text-align:center;font-style:italic;font-size:20px;line-height:30px;color:#888}
.quote-name{left:0;width:1200px;top:305px;text-align:center;font-size:15px;color:#555}
.outline-arrow{width:38px;height:38px;border:1px solid #bbb;background:#fff;display:flex;align-items:center;justify-content:center}

/* location */
.location{top:2880px;height:420px;background:var(--page)}
.map{left:180px;top:113px;width:483px;height:245px;background:linear-gradient(135deg,#cfe0c8,#e9e4d6 50%,#aecbe0)}
.contact-name{left:702px;top:125px;font-family:"Exo 2",Arial,sans-serif;font-weight:500;font-size:26px;color:#333}
.contact-row{left:702px;display:flex;gap:14px;font-size:12px;color:#777;line-height:18px}

/* associates */
.associates{top:3300px;height:320px;background:var(--page)}
.associate{top:140px;width:80px;height:70px;background:#cfd6df;border-radius:6px}

/* footer */
.site-footer{top:3620px;height:280px;background:#fff;border-top:1px solid var(--line)}
.footer-col h5{font-size:12px;text-transform:uppercase;color:#444;font-weight:600;margin-bottom:10px}
.footer-col li{list-style:none;font-size:12px;color:#888;line-height:20px}
.footer-col li::before{content:"▫ ";color:#aaa}
.copyright-bar{left:180px;top:240px;width:840px;height:1px;background:var(--line)}
.copyright{left:180px;top:252px;font-size:11px;color:#999}
.social{top:248px;width:18px;height:18px;border-radius:50%;background:#9a9a9a}
</style>
</head>
<body>

<header class="site-header">
  <div class="abs brand"><span class="brand-dot"></span><span class="brand-name">Summit Motion Wellness</span></div>
  <nav class="abs main-nav">
    <a class="active">Home</a><a>About</a><a>Services</a><a>Products</a><a>News</a><a>Contact</a><a>Log in</a>
  </nav>
  <div class="abs hero" role="img" aria-label="Photo of a pack of road cyclists racing towards the camera"></div>
</header>

<section class="about">
  <h2 class="abs section-title">About</h2>
  <p class="abs body-text" style="top:98px">Duis autem vel eum iriure dolor in hendrerit in vulputate velit esse molestie consequat, vel illum dolore eu feugiat nulla facilisis at vero eros et accumsan et iusto odio dignissim.</p>
  <p class="abs body-text" style="top:170px">Nam liber tempor cum soluta nobis eleifend option congue nihil imperdiet doming id quod mazim placerat facer possim assum. Typi non habent claritatem insitam; est usus legentis in iis qui facit eorum claritatem. Investigationes demonstraverunt lectores legere.</p>
  <div class="abs video" role="img" aria-label="Video still of a trainer in a gym">
    <div class="abs play"></div>
    <svg class="abs" style="left:194px;top:97px" width="18" height="20"><path d="M0 0 L18 10 L0 20Z" fill="#fff"/></svg>
    <div class="abs video-bar"></div>
  </div>
</section>

<section class="feature-band" style="top:950px">
  <div class="abs feature-intro">
    <h3>Our Services</h3>
    <p>Lorem ipsum dolor sit amet consectet adipiscing odio</p>
    <div class="arrows">
      <div class="arrow-btn"><svg width="8" height="12"><path d="M7 1 L2 6 L7 11" stroke="#fff" stroke-width="2" fill="none"/></svg></div>
      <div class="arrow-btn"><svg width="8" height="12"><path d="M1 1 L6 6 L1 11" stroke="#fff" stroke-width="2" fill="none"/></svg></div>
    </div>
  </div>
  <div class="abs card" style="left:396px"><div class="photo" role="img" aria-label="Photo of a physio treating a knee" style="width:195px;height:198px;background:linear-gradient(135deg,#e9c7ad,#b7876a)"></div><div class="card-label">Sports Physio</div></div>
  <div class="abs card" style="left:609px"><div class="photo" role="img" aria-label="Photo of a fit torso holding an apple" style="width:195px;height:198px;background:linear-gradient(135deg,#e2b99a,#3a3a3a 70%,#c8242c)"></div><div class="card-label">Sports Nutrition</div></div>
  <div class="abs card" style="left:822px"><div class="photo" role="img" aria-label="Photo of a foot massage" style="width:195px;height:198px;background:linear-gradient(135deg,#f1d9c7,#d6a98c)"></div><div class="card-label">Podiatry</div></div>
</section>

<section class="news">
  <h2 class="abs section-title" style="left:180px">Latest News</h2>
  <h2 class="abs section-title" style="left:606px">Pro Health Tips</h2>
  <div class="abs" style="left:180px;top:100px;width:300px;height:1px;background:var(--line)"></div>
  <div class="abs" style="left:606px;top:100px;width:414px;height:1px;background:var(--line)"></div>
  <p class="abs post-date" style="left:180px;top:120px">May 25, 2014</p>
  <p class="abs post-title" style="left:180px;top:146px;width:400px">Typi Non Habent Claritatem Insitam Est Usus</p>
  <p class="abs body-text" style="left:180px;top:225px;width:410px">Duis autem vel eum iriure dolor in hendrerit in vulputate velit esse molestie consequat, vel illum dolore eu feugiat nulla facilisis at vero eros et accumsan et iusto odio dignissim. Nam liber tempor cum soluta nobis eleifend option nihil imperdiet doming id quod mazim placerat facer possim assum.</p>
  <span class="abs btn" style="left:180px;top:345px">Read More</span>

  <p class="abs tip-title" style="left:614px;top:100px">Claritas Est Etiam Processu</p>
  <p class="abs body-text" style="left:614px;top:135px;width:400px">Duis autem vel eum iriure dolor in hendrerit in vulputate velit esse molestie consequat, vel illum.</p>
  <p class="abs tip-title" style="left:614px;top:222px">Lorem Ipsum Dolor Sit Amet</p>
  <p class="abs body-text" style="left:614px;top:257px;width:400px">Duis autem vel eum iriure dolor in hendrerit in vulputate velit esse molestie consequat, vel illum.</p>
  <span class="abs btn" style="left:606px;top:345px">Read More</span>
</section>

<section class="team">
  <div class="abs feature-intro" style="top:45px;height:195px;padding-top:30px">
    <h3>Our Team</h3>
    <p>Physio</p>
    <div class="arrows" style="top:118px">
      <div class="arrow-btn"><svg width="8" height="12"><path d="M7 1 L2 6 L7 11" stroke="#fff" stroke-width="2" fill="none"/></svg></div>
      <div class="arrow-btn"><svg width="8" height="12"><path d="M1 1 L6 6 L1 11" stroke="#fff" stroke-width="2" fill="none"/></svg></div>
    </div>
  </div>
  <div class="abs team-photo" role="img" aria-label="Photo of a smiling physiotherapist in a gym"></div>
  <div class="abs team-card">
    <h4>Lena Hartwell</h4>
    <p class="body-text">Duis autem vel eum iriure dolor in hendrerit in vulputate velit esse molestie consequat, vel illum dolore eu feugiat nulla facilisis at vero eros et accumsan et iusto odio dignissim.</p>
  </div>
</section>

<section class="testimonials">
  <h2 class="abs section-title centered-title" style="top:45px">Testimonials</h2>
  <div class="abs avatar" role="img" aria-label="Portrait of a client"></div>
  <div class="abs outline-arrow" style="left:183px;top:168px"><svg width="8" height="12"><path d="M7 1 L2 6 L7 11" stroke="#888" stroke-width="2" fill="none"/></svg></div>
  <div class="abs outline-arrow" style="left:978px;top:168px"><svg width="8" height="12"><path d="M1 1 L6 6 L1 11" stroke="#888" stroke-width="2" fill="none"/></svg></div>
  <p class="abs quote">Ut wisi enim ad minim veniam, quis nostrud exerci tation ullamcorper suscipit lobortis nisl ut aliquip ex ea commodo consequat.</p>
  <p class="abs quote-name">Maren Colfax</p>
</section>

<section class="feature-band" style="top:2500px">
  <div class="abs feature-intro">
    <h3>Our Products</h3>
    <p>Lorem ipsum dolor sit amet consectet adipiscing odio</p>
    <div class="arrows">
      <div class="arrow-btn"><svg width="8" height="12"><path d="M7 1 L2 6 L7 11" stroke="#fff" stroke-width="2" fill="none"/></svg></div>
      <div class="arrow-btn"><svg width="8" height="12"><path d="M1 1 L6 6 L1 11" stroke="#fff" stroke-width="2" fill="none"/></svg></div>
    </div>
  </div>
  <div class="abs card" style="left:396px"><div class="photo" role="img" aria-label="Photo of an ankle brace" style="width:195px;height:198px;background:linear-gradient(135deg,#f0f0f0,#5a5a5a)"></div><div class="card-label">Braces &amp; Tape</div></div>
  <div class="abs card" style="left:609px"><div class="photo" role="img" aria-label="Photo of a woman exercising on a ball" style="width:195px;height:198px;background:linear-gradient(135deg,#fafafa,#c9c9c9 60%,#9a8472)"></div><div class="card-label">Exercise Equipments</div></div>
  <div class="abs card" style="left:822px"><div class="photo" role="img" aria-label="Photo of a person resting on a support pillow" style="width:195px;height:198px;background:linear-gradient(135deg,#c9d6e8,#e5d2c4)"></div><div class="card-label">Postural Aids</div></div>
</section>

<section class="location">
  <h2 class="abs section-title centered-title" style="top:45px">Our Location</h2>
  <div class="abs map" role="img" aria-label="Street map of the clinic's area"></div>
  <p class="abs contact-name">Summit Motion Wellness</p>
  <div class="abs" style="left:702px;top:172px;width:318px;height:1px;background:var(--line)"></div>
  <div class="abs contact-row" style="top:192px"><svg width="12" height="14"><path d="M2 1 L5 1 L6 4 L4 5 Q5 8 8 10 L9 8 L12 9 L12 12 Q6 13 2 7 Q0 3 2 1Z" fill="#999"/></svg><span>(08) 5550 1937</span></div>
  <div class="abs contact-row" style="top:222px"><svg width="13" height="10"><rect x="0.5" y="0.5" width="12" height="9" fill="none" stroke="#999"/><path d="M1 1 L6.5 6 L12 1" stroke="#999" fill="none"/></svg><span>hello@summitmotionwellness.com.au</span></div>
  <div class="abs contact-row" style="top:252px"><svg width="10" height="14"><path d="M5 14 L1 7 A5 5 0 1 1 9 7Z" fill="#999"/><circle cx="5" cy="5" r="1.8" fill="#fff"/></svg><span>27 Larkspur Row,<br>Perth Western Australia</span></div>
  <span class="abs btn" style="left:702px;top:305px">Get Directions</span>
</section>

<section class="associates">
  <h2 class="abs section-title centered-title" style="top:40px">Our Associates</h2>
  <div class="abs outline-arrow" style="left:183px;top:155px"><svg width="8" height="12"><path d="M7 1 L2 6 L7 11" stroke="#888" stroke-width="2" fill="none"/></svg></div>
  <div class="abs outline-arrow" style="left:978px;top:155px"><svg width="8" height="12"><path d="M1 1 L6 6 L1 11" stroke="#888" stroke-width="2" fill="none"/></svg></div>
  <div class="abs associate" style="left:275px"></div>
  <div class="abs associate" style="left:410px"></div>
  <div class="abs associate" style="left:560px"></div>
  <div class="abs associate" style="left:700px"></div>
  <div class="abs associate" style="left:845px"></div>
</section>

<footer class="site-footer">
  <div class="abs brand" style="top:28px"><span class="brand-dot" style="width:16px;height:16px"></span><span class="brand-name" style="font-size:15px">Summit Motion Wellness</span></div>
  <p class="abs body-text" style="left:180px;top:72px;width:200px;font-size:12px;line-height:17px">Typi non habent claritatem insitam; est usus legentis in iis qui facit eorum claritatem investigationes.</p>
  <div class="abs footer-col" style="left:398px;top:30px;width:180px">
    <h5>Latest News</h5>
    <ul><li>Typi Non Habent Claritatem</li><li>Claritas Est Etiam Processu</li><li>Lorem Ipsum Dolor Sit Amet</li><li>Eodem modo typi qui nunc</li></ul>
  </div>
  <div class="abs footer-col" style="left:614px;top:30px">
    <h5>Gallery</h5>
    <div role="img" aria-label="Grid of clinic photos" style="width:190px;height:120px;background:linear-gradient(135deg,#b7c3cf,#d9b7a3 50%,#8a98a8)"></div>
  </div>
  <div class="abs footer-col" style="left:834px;top:30px">
    <h5>Links</h5>
    <ul><li>Log in | Register</li><li>Privacy Policy</li><li>Terms and Conditions</li></ul>
  </div>
  <div class="abs copyright-bar"></div>
  <p class="abs copyright">© Copyright 2014 Summit Motion Wellness</p>
  <div class="abs social" style="left:880px"></div>
  <div class="abs social" style="left:904px"></div>
  <div class="abs social" style="left:928px"></div>
  <div class="abs social" style="left:952px"></div>
  <div class="abs social" style="left:976px"></div>
  <div class="abs social" style="left:1000px"></div>
</footer>

</body>
</html>
```